Silken Roam (A luxury Travel Website)

website text attached in document below

images also attached

feel free to use other images if needed

Target Market(s)

Luxury Seekers and wealthy couples / families

Industry/Entity Type

Luxury Travel

Coding

Coded - Design and coding required

Number of Pages Required

1 page

Requirements
Must have
• A luxury design and easy use.
Nice to have
• Ease of use of page, incorporation of images into the flow of the site

```html
<!DOCTYPE html>
<html lang="en">
<head>
<meta charset="utf-8">
<title>Silken Roam — Luxury Travel</title>
<link rel="stylesheet" href="https://fonts.googleapis.com/css2?family=Playfair+Display:wght@400;700;900&family=Poppins:wght@400;500;600&display=swap">
<style>
  :root {
    --ink: #111111;
    --sky: #7db9dc;
    --navy: #24338c;
    --line: #dddddd;
    --white: #ffffff;
  }
  * { margin: 0; padding: 0; box-sizing: border-box; }
  html, body { width: 1200px; height: 3340px; overflow: hidden; background: var(--white); }
  body { position: relative; font-family: "Poppins", sans-serif; color: var(--ink); }
  .abs { position: absolute; }

  .brand { left: 0; width: 1200px; top: 30px; text-align: center; font-family: "Playfair Display", serif; font-weight: 400; font-size: 30px; letter-spacing: 1px; }
  .menu { left: 1072px; top: 36px; width: 40px; height: 32px; }
  .menu span { position: absolute; right: 0; height: 3px; background: var(--ink); border-radius: 2px; }

  .hero-title { left: 86px; top: 134px; font-family: "Playfair Display", serif; font-weight: 900; font-size: 122px; line-height: 1; letter-spacing: -1px; }

  .scroll-cue { left: 34px; top: 402px; }

  .slide-main { left: 88px; top: 403px; width: 861px; height: 547px; background: linear-gradient(180deg, #4a6fb0 0%, #5c7fa6 40%, #c98a3e 68%, #2f5fc9 85%, #1a2d5c 100%); }
  .slide-next { left: 991px; top: 403px; width: 209px; height: 547px; background: linear-gradient(135deg, #2a8a78, #3fc2c4 45%, #e9e2cf 60%, #1f9fb0); }
  .slide-prev { left: 88px; top: 876px; width: 75px; height: 74px; background: rgba(255,255,255,0.15); display: flex; align-items: center; justify-content: center; }

  .stats { left: 695px; top: 346px; width: 443px; height: 113px; background: var(--sky); color: var(--white); display: flex; align-items: center; padding-left: 42px; gap: 48px; }
  .stat { display: flex; align-items: center; gap: 10px; }
  .stat-num { font-weight: 600; font-size: 54px; line-height: 1; }
  .stat-label { font-size: 13px; line-height: 1.35; }

  .pager { left: 948px; top: 988px; width: 190px; font-size: 14px; display: flex; align-items: center; gap: 8px; }
  .pager-track { position: relative; width: 132px; height: 2px; background: var(--line); }
  .pager-track::before { content: ""; position: absolute; left: 0; top: -1px; width: 34px; height: 4px; background: var(--sky); }

  .intro-heading { left: 0; width: 1200px; top: 1056px; text-align: center; font-family: "Playfair Display", serif; font-weight: 700; font-size: 40px; line-height: 49px; }
  .rule { height: 3px; background: var(--line); }
  .intro-rule { left: 562px; top: 1220px; width: 76px; }
  .intro-text { left: 0; width: 1200px; top: 1246px; text-align: center; font-size: 16px; color: #333; }

  .cabin-photo { left: 0; top: 1365px; width: 1200px; height: 663px; background: linear-gradient(110deg, #3b2f2c 0%, #7a6a5e 35%, #d8bfa3 60%, #f3d9b5 70%, #4a3b33 100%); }
  .play { left: 1009px; top: 1974px; width: 112px; height: 112px; border-radius: 50%; background: var(--sky); display: flex; align-items: center; justify-content: center; }

  .room-photo { left: 88px; top: 2131px; width: 415px; height: 561px; background: linear-gradient(180deg, #d9d5d4 0%, #d9d5d4 24%, #6f8b63 30%, #a9bca0 50%, #6f8b63 62%, #f3f3f6 72%, #ffffff 100%); }

  .offer-heading { left: 585px; top: 2302px; font-family: "Playfair Display", serif; font-weight: 700; font-size: 40px; line-height: 49px; }
  .offer-rule { left: 585px; top: 2518px; width: 76px; }
  .btn-book { left: 585px; top: 2557px; width: 210px; height: 52px; background: var(--sky); color: var(--white); font-weight: 600; font-size: 14px; display: flex; align-items: center; justify-content: center; gap: 16px; }

  .skyline { left: 0; top: 2790px; width: 1200px; height: 160px; background: linear-gradient(180deg, rgba(36,51,140,0.25) 0%, rgba(36,51,140,0.75) 50%, var(--navy) 100%); }
  .footer { left: 0; top: 2950px; width: 1200px; height: 390px; background: var(--navy); color: var(--white); }
  .footer-heading { left: 0; width: 1200px; top: 80px; text-align: center; font-family: "Playfair Display", serif; font-weight: 700; font-size: 33px; }
  .footer-sub { left: 0; width: 1200px; top: 128px; text-align: center; font-family: "Playfair Display", serif; font-weight: 700; font-size: 16px; letter-spacing: 0.5px; }
  .signup { left: 242px; top: 186px; width: 716px; height: 52px; display: flex; }
  .signup-field { flex: 1; background: var(--white); color: #777; font-size: 14px; display: flex; align-items: center; gap: 12px; padding-left: 28px; }
  .signup-submit { width: 150px; background: var(--sky); color: var(--white); font-weight: 600; font-size: 15px; display: flex; align-items: center; justify-content: center; gap: 12px; }
  .footer-line { left: 88px; top: 324px; width: 1024px; height: 1px; background: rgba(255,255,255,0.25); }
  .to-top { left: 1131px; top: 300px; width: 44px; height: 44px; background: var(--sky); display: flex; align-items: center; justify-content: center; }
  .copyright { left: 0; width: 1200px; top: 344px; text-align: center; font-size: 14px; font-weight: 500; }
</style>
</head>
<body>

<header>
  <div class="abs brand">Silken Roam</div>
  <div class="abs menu" aria-label="Menu">
    <span style="top:2px;width:36px"></span>
    <span style="top:14px;width:24px"></span>
    <span style="top:26px;width:36px"></span>
  </div>
</header>

<h1 class="abs hero-title">SILKEN ROAM</h1>

<svg class="abs scroll-cue" width="20" height="48" viewBox="0 0 20 48" aria-hidden="true">
  <path d="M10 0 V46 M1 37 L10 46 L19 37" fill="none" stroke="#aaaaaa" stroke-width="2"/>
</svg>

<section class="hero-slider">
  <div class="abs slide-main" role="img" aria-label="Tropical resort pool at dusk with palm trees and lit villa"></div>
  <div class="abs slide-next" role="img" aria-label="Aerial view of an island beach with overwater villas"></div>
  <div class="abs slide-prev">
    <svg width="26" height="18" viewBox="0 0 26 18" aria-hidden="true"><path d="M25 9 H2 M9 1 L1 9 L9 17" fill="none" stroke="#fff" stroke-width="2"/></svg>
  </div>
  <div class="abs stats">
    <div class="stat"><span class="stat-num">10</span><span class="stat-label">Years<br>Experiences</span></div>
    <div class="stat"><span class="stat-num">25</span><span class="stat-label">Partner<br>Collaboration</span></div>
  </div>
  <div class="abs pager"><span>01</span><span class="pager-track"></span><span>03</span></div>
</section>

<section class="intro">
  <h2 class="abs intro-heading">LOOKING TO STAY AT A 5 STAR<br>HOTEL OR TO FLY BUSINESS CLASS<br>ANYWHERE?</h2>
  <div class="abs rule intro-rule"></div>
  <p class="abs intro-text">Share a screenshot of your travel plans and we beat the price, within 24 hours.</p>
</section>

<section class="cabin">
  <div class="abs cabin-photo" role="img" aria-label="Business class cabin with a flight attendant and a passenger pouring tea"></div>
  <div class="abs play" aria-label="Play video">
    <svg width="22" height="24" viewBox="0 0 22 24" aria-hidden="true"><path d="M2 1 L21 12 L2 23 Z" fill="#fff"/></svg>
  </div>
</section>

<section class="offer">
  <div class="abs room-photo" role="img" aria-label="Hotel bedroom with a white bed and green leaf wallpaper"></div>
  <h2 class="abs offer-heading">WE WORK DIRECTLY WITH<br>HOTELS AND AIRLINES TO<br>GET YOU THE BEST PRICE,<br>ALWAYS.</h2>
  <div class="abs rule offer-rule"></div>
  <div class="abs btn-book">BOOKING NOW
    <svg width="26" height="18" viewBox="0 0 26 18" aria-hidden="true"><path d="M1 9 H24 M17 1 L25 9 L17 17" fill="none" stroke="#fff" stroke-width="2"/></svg>
  </div>
</section>

<div class="abs skyline" role="img" aria-label="Skyline of world landmarks in navy silhouette"></div>

<footer class="abs footer">
  <h2 class="abs footer-heading">TELL US ABOUT YOUR NEXT HOLIDAY PLANS</h2>
  <p class="abs footer-sub">THE MORE DETAILS THE BETTER.</p>
  <div class="abs signup">
    <div class="signup-field">
      <svg width="18" height="13" viewBox="0 0 18 13" aria-hidden="true"><rect x="0.5" y="0.5" width="17" height="12" fill="#bbb"/><path d="M1 1 L9 7 L17 1" fill="none" stroke="#fff" stroke-width="1.5"/></svg>
      Enter your email address...
    </div>
    <div class="signup-submit">SUBMIT
      <svg width="16" height="16" viewBox="0 0 16 16" aria-hidden="true"><path d="M15 1 L1 7 L6 9 L8 15 Z M15 1 L6 9" fill="#fff" stroke="#fff" stroke-width="1" stroke-linejoin="round"/></svg>
    </div>
  </div>
  <div class="abs footer-line"></div>
  <div class="abs to-top" aria-label="Back to top">
    <svg width="16" height="20" viewBox="0 0 16 20" aria-hidden="true"><path d="M8 19 V2 M1 9 L8 2 L15 9" fill="none" stroke="#fff" stroke-width="1.8"/></svg>
  </div>
  <p class="abs copyright">© Copyright Silken Roam All Rights Reserved</p>
</footer>

</body>
</html>
```